Kestrel Drafts (Residential House Plans Company)

Want professional landing page to match our company theme. We provide custom house plans for primarily residential. We are structural engineers (not architects).

Prefer dark (black) theme but open to design options. Would like map of office location.

Address: 214 W Marlow Street, Larkmoor, FL 30412
Phone: 555-582-6194
Email: office@kestreldrafts.example

Target Market(s)

Client who need custom house plans

Industry/Entity Type

Architecture, Structural Engineering

Coding

Coded - Design and coding required

Colors
0054AA
0677BA
7BADD7
CADEEF
E8F1F8

```html
<!DOCTYPE html>
<html lang="en">
<head>
<meta charset="UTF-8">
<title>Kestrel Drafts — Custom House Plans</title>
<link rel="stylesheet" href="https://fonts.googleapis.com/css2?family=Poppins:wght@300;400;500;600&display=swap">
<style>
:root{
  --bg:#04070c;
  --blue-deep:#0054AA;
  --blue:#0677BA;
  --blue-mid:#7BADD7;
  --blue-pale:#CADEEF;
  --blue-mist:#E8F1F8;
  --text:#ffffff;
  --muted:#9aa8b6;
  --line:rgba(123,173,215,.28);
}
*{margin:0;padding:0;box-sizing:border-box}
html,body{width:1200px;height:3600px;overflow:hidden}
body{background:var(--bg);color:var(--text);font-family:'Poppins',sans-serif;position:relative}
.abs{position:absolute}
a{color:inherit;text-decoration:none}

/* nav */
.brand{font-weight:600;font-size:24px;letter-spacing:.5px;color:var(--text)}
.site-nav{left:108px;top:30px;width:992px;display:flex;justify-content:space-between;align-items:center}
.nav-links{display:flex;gap:34px;font-size:15px;color:var(--blue-mist)}

/* shared */
.btn{display:inline-flex;align-items:center;justify-content:center;height:40px;padding:0 26px;border-radius:20px;font-size:14px;font-weight:500}
.btn-solid{background:var(--blue);color:#fff}
.btn-ghost{border:1px solid var(--blue);color:var(--blue-mid)}
.eyebrow{font-size:17px;color:var(--blue-pale)}
.section-title{font-size:38px;font-weight:500;line-height:1.25}
.body-copy{font-size:14px;line-height:1.7;color:var(--muted)}
.ph{border-radius:4px}

/* hero */
.hero-copy{left:108px;top:170px;width:540px}
.hero-title{font-size:56px;font-weight:500;line-height:1.2}
.hero-copy .body-copy{margin-top:20px;width:470px}
.hero-actions{margin-top:26px;display:flex;gap:18px}
.hero-glow{left:-200px;top:-100px;width:900px;height:800px;background:radial-gradient(circle at 30% 40%,rgba(6,119,186,.22),transparent 60%)}
.photo-main{left:700px;top:140px;width:210px;height:400px;background:linear-gradient(160deg,#6f95b8,#2b4a66 55%,#1a2a3a);border:3px solid var(--blue)}
.photo-fade{left:910px;top:140px;width:260px;height:200px;background:linear-gradient(120deg,#0c1520,#1c2e42)}
.photo-side{left:930px;top:330px;width:230px;height:210px;background:linear-gradient(160deg,#b7c9d8,#6d7f86 50%,#4a3a2d)}

/* about */
.blueprint{left:120px;top:660px;width:440px;height:330px;background:radial-gradient(ellipse at 45% 55%,rgba(6,119,186,.45),rgba(0,84,170,.08) 70%,transparent)}
.about-copy{left:608px;top:680px;width:470px}
.about-copy .section-title{margin-top:12px}
.about-copy .body-copy{margin-top:14px;font-size:13px}
.about-copy .btn{margin-top:20px}

/* newsletter */
.newsletter{left:188px;top:1100px;width:820px;height:240px;border-radius:22px;background:linear-gradient(120deg,var(--blue-deep),var(--blue) 55%,#5d9cd1);padding:36px 48px;overflow:hidden}
.newsletter .eyebrow{font-size:13px;color:var(--blue-mist)}
.newsletter h2{margin-top:18px;font-size:34px;font-weight:500;line-height:1.2;width:360px}
.subscribe{margin-top:18px;display:flex;width:720px;height:44px}
.subscribe input{flex:1;border:0;border-radius:4px 0 0 4px;padding:0 18px;font-family:inherit;font-size:13px;color:#667}
.subscribe button{width:140px;border:0;border-radius:0 4px 4px 0;background:var(--blue-deep);color:#fff;font-family:inherit;font-size:14px}
.newsletter-house{right:40px;top:20px;width:300px;height:130px;opacity:.35;background:radial-gradient(ellipse,rgba(232,241,248,.35),transparent 70%)}

/* plans */
.plans-head{left:200px;top:1430px;width:800px;text-align:center}
.plans-head .section-title{margin-top:10px;font-size:34px}
.plans-head .body-copy{margin-top:12px}
.plan-card{top:1620px;width:322px;height:610px;border-radius:26px;border:1px solid var(--line);background:linear-gradient(170deg,rgba(12,24,38,.95),rgba(4,8,14,.95));padding:34px 30px}
.plan-name{font-size:18px;color:var(--blue-mist)}
.plan-price{font-size:36px;font-weight:500;margin-top:8px;padding-bottom:22px;border-bottom:1px solid var(--line)}
.plan-features{list-style:none;margin-top:30px}
.plan-features li{display:flex;align-items:center;gap:12px;font-size:12px;color:var(--blue-pale);height:60px;white-space:nowrap}
.tick{width:20px;height:20px;flex:none}
.plan-card .btn{position:absolute;left:50%;bottom:40px;transform:translateX(-50%);height:36px;font-size:13px}
.orb{border-radius:50%;background:radial-gradient(circle at 35% 35%,#6fb3ef,var(--blue) 45%,var(--blue-deep))}

/* projects */
.projects-copy{left:108px;top:2340px;width:440px}
.projects-copy .section-title{margin-top:12px;font-size:36px}
.projects-copy .body-copy{margin-top:14px}
.projects-copy .btn{margin-top:24px}
.work-a{left:608px;top:2330px;width:484px;height:290px;background:linear-gradient(160deg,#c9b9a3,#7c6a55 50%,#2f5f7a)}
.work-b{left:108px;top:2660px;width:484px;height:280px;background:linear-gradient(170deg,#8ab3d6,#d9d4c8 55%,#4f5f4a)}
.work-c{left:608px;top:2660px;width:484px;height:280px;background:linear-gradient(160deg,#1a2a38,#3a4d5c 50%,#1b4c6e)}

/* contact */
.map{left:0;top:3040px;width:520px;height:300px;background:linear-gradient(135deg,#dfe7ee,#c4d3df 60%,#aebfcd);border:4px solid var(--blue)}
.contact-copy{left:608px;top:3040px;width:500px}
.contact-copy .section-title{margin-top:10px;font-size:36px}
.contact-list{list-style:none;margin-top:24px}
.contact-list li{display:flex;align-items:center;gap:14px;font-size:14px;color:var(--blue-pale);height:50px}
.contact-icon{width:30px;height:30px;border-radius:50%;background:var(--blue);display:flex;align-items:center;justify-content:center;flex:none}

/* footer */
.site-footer{left:108px;top:3470px;width:984px;display:flex;justify-content:space-between;align-items:center}
.footer-links{display:flex;gap:30px;font-size:14px;color:var(--blue-mist)}
.socials{display:flex;gap:18px}
.socials span{width:34px;height:34px;border-radius:50%;background:var(--blue)}
.footer-rule{left:108px;top:3540px;width:984px;height:1px;background:var(--line)}
.copyright{left:0;top:3560px;width:1200px;text-align:center;font-size:12px;color:var(--muted)}
</style>
</head>
<body>

<div class="abs hero-glow"></div>

<header class="abs site-nav">
  <a class="brand" href="#">Kestrel Drafts</a>
  <nav class="nav-links"><a href="#">Home</a><a href="#">About</a><a href="#">Plans</a><a href="#">Projects</a><a href="#">Contact</a></nav>
</header>

<section>
  <div class="abs hero-copy">
    <h1 class="hero-title">We Provide Custom Plans For Your Dream House</h1>
    <p class="body-copy">Structural engineers drafting residential plans that are clear, permit ready and shaped around the way your family lives.</p>
    <div class="hero-actions"><a class="btn btn-solid" href="#">Learn More</a><a class="btn btn-ghost" href="#">View Plans</a></div>
  </div>
  <div class="abs ph photo-fade" role="img" aria-label="Faded photo of a house under construction"></div>
  <div class="abs ph photo-side" role="img" aria-label="Photo of a couple looking at a new house"></div>
  <div class="abs ph photo-main" role="img" aria-label="Photo of engineers on a building site with cranes"></div>
</section>

<section>
  <div class="abs blueprint" role="img" aria-label="Glowing blue technical drawing of a house"></div>
  <div class="abs about-copy">
    <p class="eyebrow">About</p>
    <h2 class="section-title">Know What Make Us Different From Others</h2>
    <p class="body-copy">We are licensed structural engineers, not architects, so every plan starts with sound framing, loads and foundations. Our drafts are checked for local code, priced up front and revised until the layout feels right to you and your builder.</p>
    <a class="btn btn-solid" href="#">Learn More</a>
  </div>
</section>

<section class="abs newsletter">
  <div class="abs newsletter-house" role="img" aria-label="Faint line drawing of a house"></div>
  <p class="eyebrow">Subscribe Our Newsletter</p>
  <h2>Subscribe To Don't Miss An Update</h2>
  <form class="subscribe"><input type="email" placeholder="youremail@example.com"><button type="button">Subscribe</button></form>
</section>

<section>
  <div class="abs plans-head">
    <p class="eyebrow">Plans</p>
    <h2 class="section-title">Choose The Right Plan For Your Need</h2>
    <p class="body-copy">Every package includes engineered drawings, code review and revisions. Pick the level of detail your project needs today.</p>
  </div>

  <div class="abs orb" style="left:60px;top:1660px;width:90px;height:90px"></div>
  <div class="abs orb" style="left:1040px;top:2050px;width:110px;height:110px"></div>

  <article class="abs plan-card" style="left:100px">
    <p class="plan-name">Basic</p>
    <p class="plan-price">499$</p>
    <ul class="plan-features">
      <li><svg class="tick" viewBox="0 0 20 20"><circle cx="10" cy="10" r="10" fill="#0677BA"/><path d="M6 10.5l2.7 2.7L14 7.8" stroke="#fff" stroke-width="2" fill="none"/></svg>Amet Consectetur Neque Faucibus</li>
      <li><svg class="tick" viewBox="0 0 20 20"><circle cx="10" cy="10" r="10" fill="#0677BA"/><path d="M6 10.5l2.7 2.7L14 7.8" stroke="#fff" stroke-width="2" fill="none"/></svg>Amet Neque Faucibus</li>
      <li><svg class="tick" viewBox="0 0 20 20"><circle cx="10" cy="10" r="10" fill="#0677BA"/><path d="M6 10.5l2.7 2.7L14 7.8" stroke="#fff" stroke-width="2" fill="none"/></svg>Amet Neque Faucibus</li>
      <li><svg class="tick" viewBox="0 0 20 20"><circle cx="10" cy="10" r="10" fill="#0677BA"/><path d="M6 10.5l2.7 2.7L14 7.8" stroke="#fff" stroke-width="2" fill="none"/></svg>Amet Consectetur Neque Faucibus</li>
    </ul>
    <a class="btn btn-solid" href="#">Get Started</a>
  </article>

  <article class="abs plan-card" style="left:439px">
    <p class="plan-name">Pro</p>
    <p class="plan-price">999$</p>
    <ul class="plan-features">
      <li><svg class="tick" viewBox="0 0 20 20"><circle cx="10" cy="10" r="10" fill="#0677BA"/><path d="M6 10.5l2.7 2.7L14 7.8" stroke="#fff" stroke-width="2" fill="none"/></svg>Amet Consectetur Neque Faucibus</li>
      <li><svg class="tick" viewBox="0 0 20 20"><circle cx="10" cy="10" r="10" fill="#0677BA"/><path d="M6 10.5l2.7 2.7L14 7.8" stroke="#fff" stroke-width="2" fill="none"/></svg>Amet Neque Faucibus</li>
      <li><svg class="tick" viewBox="0 0 20 20"><circle cx="10" cy="10" r="10" fill="#0677BA"/><path d="M6 10.5l2.7 2.7L14 7.8" stroke="#fff" stroke-width="2" fill="none"/></svg>Amet Neque Faucibus</li>
      <li><svg class="tick" viewBox="0 0 20 20"><circle cx="10" cy="10" r="10" fill="#0677BA"/><path d="M6 10.5l2.7 2.7L14 7.8" stroke="#fff" stroke-width="2" fill="none"/></svg>Amet Neque Faucibus</li>
      <li><svg class="tick" viewBox="0 0 20 20"><circle cx="10" cy="10" r="10" fill="#0677BA"/><path d="M6 10.5l2.7 2.7L14 7.8" stroke="#fff" stroke-width="2" fill="none"/></svg>Amet Consectetur Neque Faucibus</li>
    </ul>
    <a class="btn btn-solid" href="#">Get Started</a>
  </article>

  <article class="abs plan-card" style="left:778px">
    <p class="plan-name">Ultimate</p>
    <p class="plan-price">1499$</p>
    <ul class="plan-features">
      <li><svg class="tick" viewBox="0 0 20 20"><circle cx="10" cy="10" r="10" fill="#0677BA"/><path d="M6 10.5l2.7 2.7L14 7.8" stroke="#fff" stroke-width="2" fill="none"/></svg>Amet Consectetur Neque Faucibus</li>
      <li><svg class="tick" viewBox="0 0 20 20"><circle cx="10" cy="10" r="10" fill="#0677BA"/><path d="M6 10.5l2.7 2.7L14 7.8" stroke="#fff" stroke-width="2" fill="none"/></svg>Amet Neque Faucibus</li>
      <li><svg class="tick" viewBox="0 0 20 20"><circle cx="10" cy="10" r="10" fill="#0677BA"/><path d="M6 10.5l2.7 2.7L14 7.8" stroke="#fff" stroke-width="2" fill="none"/></svg>Amet Neque Faucibus</li>
      <li><svg class="tick" viewBox="0 0 20 20"><circle cx="10" cy="10" r="10" fill="#0677BA"/><path d="M6 10.5l2.7 2.7L14 7.8" stroke="#fff" stroke-width="2" fill="none"/></svg>Amet Neque Faucibus</li>
      <li><svg class="tick" viewBox="0 0 20 20"><circle cx="10" cy="10" r="10" fill="#0677BA"/><path d="M6 10.5l2.7 2.7L14 7.8" stroke="#fff" stroke-width="2" fill="none"/></svg>Amet Consectetur Neque Faucibus</li>
      <li><svg class="tick" viewBox="0 0 20 20"><circle cx="10" cy="10" r="10" fill="#0677BA"/><path d="M6 10.5l2.7 2.7L14 7.8" stroke="#fff" stroke-width="2" fill="none"/></svg>Amet Consectetur Neque Faucibus</li>
    </ul>
    <a class="btn btn-solid" href="#">Get Started</a>
  </article>
</section>

<section>
  <div class="abs projects-copy">
    <p class="eyebrow">Projects</p>
    <h2 class="section-title">Explore Our Best Works</h2>
    <p class="body-copy">A look at recent homes built from our plans, from compact lake cottages to modern two story family residences.</p>
    <a class="btn btn-solid" href="#">Learn More</a>
  </div>
  <div class="abs ph work-a" role="img" aria-label="Photo of a modern stone and wood house with a pool"></div>
  <div class="abs ph work-b" role="img" aria-label="Photo of a white modern house with palm trees"></div>
  <div class="abs ph work-c" role="img" aria-label="Photo of a modern house at dusk with a lit pool"></div>
</section>

<section>
  <div class="abs map" role="img" aria-label="Street map showing the office location in Larkmoor"></div>
  <div class="abs contact-copy">
    <p class="eyebrow">Contact</p>
    <h2 class="section-title">Connect With Us To Make Your Dream House</h2>
    <ul class="contact-list">
      <li><span class="contact-icon"><svg width="14" height="14" viewBox="0 0 24 24"><path d="M12 2a7 7 0 0 0-7 7c0 5 7 13 7 13s7-8 7-13a7 7 0 0 0-7-7zm0 9.5A2.5 2.5 0 1 1 12 6.5a2.5 2.5 0 0 1 0 5z" fill="#fff"/></svg></span>214 W Marlow Street, Larkmoor, FL 30412</li>
      <li><span class="contact-icon"><svg width="14" height="14" viewBox="0 0 24 24"><path d="M6.6 10.8a15 15 0 0 0 6.6 6.6l2.2-2.2a1 1 0 0 1 1-.25 11.4 11.4 0 0 0 3.6.57 1 1 0 0 1 1 1V20a1 1 0 0 1-1 1A17 17 0 0 1 3 4a1 1 0 0 1 1-1h3.5a1 1 0 0 1 1 1c0 1.25.2 2.45.57 3.57a1 1 0 0 1-.25 1z" fill="#fff"/></svg></span>555-582-6194</li>
      <li><span class="contact-icon"><svg width="14" height="14" viewBox="0 0 24 24"><rect x="3" y="5" width="18" height="14" rx="2" fill="#fff"/><path d="M3 7l9 6 9-6" stroke="#0677BA" stroke-width="2" fill="none"/></svg></span>office@kestreldrafts.example</li>
    </ul>
  </div>
</section>

<footer>
  <div class="abs site-footer">
    <a class="brand" href="#">Kestrel Drafts</a>
    <nav class="footer-links"><a href="#">Home</a><a href="#">About</a><a href="#">Plans</a><a href="#">Projects</a><a href="#">Contact</a></nav>
    <div class="socials"><span></span><span></span><span></span></div>
  </div>
  <div class="abs footer-rule"></div>
  <p class="abs copyright">© 2024 Kestrel Drafts. All rights reserved.</p>
</footer>

</body>
</html>
```